Landing Page Design for Fellas Past Fifty

I have an exercise book that I sell through Instagram. One of my teaching concepts has grow to be running joke yet valuable because it really works. It’s called the Quick Tick Quest. Its purpose is to create a habit / a daily habit of exercise by starting with just 10 seconds a day but doing it everyday for 30 days. After the habit is established the time is increased. Ten seconds is such a ridiculous amount of exercise time but help establish the habit. We need a landing page; sexy, eye catching for guys, FUN with a touch of tease. Classy not as “Tacky LasVegas” as the attached. Fellas PastFifty were born 1960 to 1975.
Change copy slightly as you see fit. We will run an Simple Instagram Ad with the headline

“ FellasPastFifty
out of shape & overweight
Discover Insanely Simple Steps
to Get You in Shape Before Your Health Deteriorates,
You Develop Diabetes,
Have a Stroke & Die Way Too Early.
Learn More

from this IG Ad they will go to the landing page. A coordinating layout of this IG ad would be nice also.
I have attached the copy for the landing page and a “Tacky” design; again I need sexy but more classy. I want to catch the attention of guys.
Thank you_Bo
PS: I need a long term relationship to make future copy adjustments and hopefully you have the ability to make the site go live with a connection to my samcart or another site for purchases. Looking forward to your design.

Target Market(s)

Men / Fellas Past Fifty

Industry/Entity Type

Health And Wellness

Number of Pages Required

1 page

Font styles to use
Sans Serif

Requirements
Must have
• A simple classy sexy design with Eye appeal to Fellas Past Fifty

I own these two websites
www.FellasPastFifty.com www.TheQuickTickQuest.com
Nice to have
• Long term relationship for this project and future projects.
I'm an entrepreneur in need of tech support.
Should not have
• Should not have Too much clutter and not be tacky

```html
<!DOCTYPE html>
<html lang="en">
<head>
<meta charset="utf-8">
<title>Quick Tick Quest – Fellas Past Fifty</title>
<link rel="stylesheet" href="https://fonts.googleapis.com/css2?family=Fira+Sans:wght@300;400;600;700;800&family=Russo+One&display=swap">
<style>
  :root {
    --magenta: #b51fa3;
    --hot-pink: #f0176d;
    --deep-violet: #5a1670;
    --plum: #7c1470;
    --lemon: #f2e531;
    --mustard: #dcd02c;
    --white: #ffffff;
    --shadow-violet: #3a0d4a;
  }
  * { margin: 0; padding: 0; box-sizing: border-box; }
  html, body { width: 1161px; height: 1200px; overflow: hidden; }
  body { font-family: "Fira Sans", sans-serif; color: var(--white); background: var(--magenta); }

  .landing {
    position: relative; width: 1161px; height: 1200px; overflow: hidden;
    background: linear-gradient(100deg, var(--magenta) 0%, #d21b8d 45%, var(--hot-pink) 100%);
  }
  .decor { position: absolute; inset: 0; width: 100%; height: 100%; }

  .photo { position: absolute; }
  .photo--athlete-left {
    left: 0; top: 95px; width: 300px; height: 1105px;
    background: linear-gradient(180deg, rgba(70,10,80,.55) 0%, rgba(110,20,120,.45) 50%, rgba(90,20,110,.5) 100%);
    clip-path: polygon(35% 0, 75% 3%, 100% 30%, 95% 55%, 70% 75%, 60% 100%, 0 100%, 0 8%);
  }
  .photo--runner-right {
    right: 0; top: 55px; width: 280px; height: 480px;
    background: linear-gradient(180deg, rgba(60,20,50,.5), rgba(80,80,100,.45));
    clip-path: polygon(55% 0, 80% 8%, 100% 20%, 100% 100%, 55% 100%, 40% 60%, 10% 45%, 40% 25%);
  }
  .photo--dumbbell-band {
    left: 310px; top: 500px; width: 190px; height: 150px; border-radius: 50%;
    background: radial-gradient(circle, rgba(90,20,120,.6), rgba(90,20,120,0) 70%);
  }
  .photo--athlete-right {
    right: 0; top: 690px; width: 240px; height: 510px;
    background: linear-gradient(180deg, rgba(70,15,70,.45), rgba(40,10,50,.6));
    clip-path: polygon(45% 0, 80% 2%, 100% 10%, 100% 100%, 20% 100%, 10% 70%, 25% 30%);
  }

  .headline-block { position: absolute; left: 0; top: 0; width: 1161px; text-align: center; }
  .quest-title {
    position: absolute; top: 52px; width: 100%;
    font-family: "Russo One", sans-serif; font-size: 34px; letter-spacing: 1px;
    color: var(--white); transform: skewX(-12deg);
  }
  .audience {
    position: absolute; top: 114px; width: 100%;
    font-weight: 700; font-size: 58px; letter-spacing: 1px;
  }
  .pain-point {
    position: absolute; top: 200px; width: 100%;
    font-weight: 700; font-size: 37px; color: var(--lemon);
  }
  .pitch {
    position: absolute; top: 270px; left: 250px; width: 660px;
    font-weight: 300; font-size: 23px; line-height: 32px;
  }
  .goal {
    position: absolute; top: 430px; width: 100%;
    font-weight: 700; font-size: 22px;
  }
  .lead-in {
    position: absolute; top: 474px; width: 100%;
    font-weight: 700; font-size: 22px;
  }

  .quest-band {
    position: absolute; left: 0; top: 534px; width: 1161px; height: 77px;
    background: var(--mustard);
    display: flex; align-items: center; justify-content: center;
    font-weight: 800; font-size: 50px; color: var(--plum); letter-spacing: .5px;
  }

  .challenge { position: absolute; left: 140px; top: 666px; width: 440px; }
  .challenge__question { font-weight: 700; font-size: 23px; line-height: 32px; }
  .challenge__note { margin-top: 24px; font-weight: 300; font-size: 16px; line-height: 26px; }

  .tips-card { position: absolute; left: 140px; top: 836px; width: 431px; }
  .tips-card__photo {
    height: 219px;
    background: linear-gradient(120deg, #8a6b58 0%, #c89a7a 40%, #f4e3c8 75%, #e8d8c4 100%);
  }
  .tips-card__label {
    height: 50px; background: var(--mustard);
    display: flex; align-items: center; justify-content: center;
    font-weight: 800; font-size: 28px; color: var(--magenta);
  }

  .offer { position: absolute; left: 652px; top: 665px; width: 380px; }
  .offer__heading { font-weight: 700; font-size: 30px; letter-spacing: .5px; }
  .pill-button {
    display: inline-flex; align-items: center; justify-content: center;
    border: 3px solid var(--white); border-radius: 30px;
    font-weight: 700; color: var(--white); background: transparent;
  }
  .offer__buy { margin-top: 18px; width: 112px; height: 51px; font-size: 20px; }
  .offer__encourage {
    margin-top: 36px; font-weight: 300; font-size: 16px; line-height: 26.5px;
  }

  .book-offer { position: absolute; left: 654px; top: 925px; width: 380px; height: 160px; }
  .book-offer__cover {
    position: absolute; left: 0; top: 0; width: 103px; height: 158px;
    background: linear-gradient(180deg, #f5b221, #e69d10);
    border-right: 6px solid #2b2b2b; border-left: 3px solid #555;
    box-shadow: 3px 4px 6px rgba(0,0,0,.35);
    transform: skewY(4deg);
  }
  .book-offer__title {
    position: absolute; left: 151px; top: 4px;
    font-weight: 700; font-size: 31px; line-height: 39px;
  }
  .book-offer__cart { position: absolute; left: 152px; top: 97px; width: 192px; height: 51px; font-size: 20px; }
</style>
</head>
<body>
<main class="landing">
  <svg class="decor" viewBox="0 0 1161 1200" aria-hidden="true">
    <polygon points="840,250 1161,0 1161,540" fill="#e0147a" opacity=".55"/>
    <polygon points="200,1200 530,1105 760,1200" fill="#e81a6f" opacity=".7"/>
    <polygon points="0,1030 140,930 140,1200 0,1200" fill="#a81c9c" opacity=".5"/>
  </svg>

  <div class="photo photo--athlete-left" role="img" aria-label="Fit woman in a black sports top training with a dumbbell"></div>
  <div class="photo photo--runner-right" role="img" aria-label="Athletic woman in camo leggings mid stride"></div>
  <div class="photo photo--dumbbell-band" role="img" aria-label="Dumbbell behind the challenge banner"></div>
  <div class="photo photo--athlete-right" role="img" aria-label="Woman in workout wear holding dumbbells"></div>

  <header class="headline-block">
    <p class="quest-title">QUICK TICK QUEST</p>
    <h1 class="audience">FELLAS PAST FIFTY</h1>
    <p class="pain-point">Out of shape and overweight</p>
    <p class="pitch">Discover The Quick Tick Quest Plus Dozens of Insanely Simple Steps to Get You in Shape Before Your Health Deteriorates, You Develop Diabetes, Have a Stroke &amp; Die Way Too Early.</p>
    <p class="goal">Our Goal is to Get You Healthy.Wanna Know Our Secret?</p>
    <p class="lead-in">It starts with the</p>
  </header>

  <h2 class="quest-band">THE QUICK TICK QUEST</h2>

  <section class="challenge">
    <p class="challenge__question">Think You Can Last a Full 10 Seconds?<br>Are you up for it?</p>
    <p class="challenge__note">You Don’t Need to Kill Yourself with Exercise<br>and You Don’t Need to Starve with an extreme Diet.</p>
  </section>

  <section class="tips-card">
    <div class="tips-card__photo" role="img" aria-label="Woman drinking water in a sunlit gym"></div>
    <p class="tips-card__label">FREE TIPS</p>
  </section>

  <section class="offer">
    <h3 class="offer__heading">NO MORE EXCUSES</h3>
    <span class="pill-button offer__buy">BUY</span>
    <p class="offer__encourage">I’m not ready for a Quick Tick Quest<br>I need more encouragement Then Text HELP to<br>47474 to get FREE tips that make<br>a difference in your health and get your ass in gear.</p>
  </section>

  <section class="book-offer">
    <div class="book-offer__cover" role="img" aria-label="Exercise book cover with a smiling trainer"></div>
    <h3 class="book-offer__title">PURCHASE<br>A BOOK</h3>
    <span class="pill-button book-offer__cart">ADD TO CART</span>
  </section>
</main>
</body>
</html>
```